small business website design

***Update: need the design to be coded into a wordpress or similar format***
Need a website for a small business with big plans. No online ordering etc but business description and contact details pages, a page showing products we use and page for customers or suppliers to register with us. Also want links to chirpnest. We have a logo existing but also open to any improvements on the design. We have an existing website we created and looks very DIY but you can get some info from it to help create your design for us.
Hi Everyone, we didn't make it clear at the beginning but we would like the final design to be in a coded format and ready to upload to a URL. I have to apologise and admit to my lack of knowledge of the design process.
Oil / gas and industrial plant managers.
Small Business

```html
<!DOCTYPE html>
<html lang="en">
<head>
<meta charset="utf-8">
<title>Meridian Gauging Services</title>
<link rel="stylesheet" href="https://fonts.googleapis.com/css2?family=Source+Sans+3:wght@400;600&display=swap">
<style>
:root{
  --blue:#2a94c6;
  --ink:#2b2b2b;
  --text:#333;
  --muted:#555;
  --panel:#f4f4f4;
  --footer:#333;
  --footer-dark:#262626;
  --rule:#cfcfcf;
  --footer-mark:#9a9a9a;
}
*{box-sizing:border-box;margin:0;padding:0}
html,body{width:1108px;height:1200px;overflow:hidden;background:#fff}
body{position:relative;font-family:Arial,Helvetica,sans-serif;color:var(--text)}
.site-header{position:absolute;left:0;top:0;width:1108px;height:115px}
.brand{position:absolute;left:92px;top:30px;display:flex;align-items:center;gap:10px;font-family:"Source Sans 3",sans-serif;font-weight:600;font-size:24px;color:var(--blue)}
.brand-dot{width:44px;height:44px;border-radius:50%;background:var(--blue)}
.main-nav{position:absolute;right:98px;top:25px;font-size:12.5px;color:#333;letter-spacing:.3px}
.main-nav span{margin:0 12px}
.search{position:absolute;left:738px;top:55px;width:277px;height:35px;border:1px solid #ccc;background:#fff;font-family:"Source Sans 3",sans-serif;font-size:15px;color:#999;padding:8px 11px}
.search svg{position:absolute;right:9px;top:9px}
.header-rule{position:absolute;left:0;top:115px;width:1108px;height:4px;background:var(--blue);border-top:1px dotted #7cc}
.hero{position:absolute;left:0;top:119px;width:1108px;height:408px;background:linear-gradient(180deg,#8fa6c9 0%,#c9d3df 30%,#e8ecef 45%,#6b5a4a 62%,#8c7c6c 72%,#c9ccd0 85%,#a8b2bc 100%)}
.hero-box{position:absolute;left:92px;top:68px;width:393px;height:207px;background:rgba(40,40,40,.93);padding:16px 21px;color:#fff;font-family:"Source Sans 3",sans-serif}
.hero-box h1{font-weight:400;font-size:36px;line-height:40px;margin-bottom:8px}
.hero-box h1 em{font-style:normal;color:var(--blue)}
.hero-box li{list-style:none;font-size:15px;line-height:20.3px;letter-spacing:.3px;padding-left:13px;position:relative}
.hero-box li::before{content:"";position:absolute;left:0;top:7px;border-left:4px solid #fff;border-top:3px solid transparent;border-bottom:3px solid transparent}
.intro{position:absolute;left:0;top:527px;width:1108px;height:268px;background:var(--panel)}
.intro-col{position:absolute;top:30px}
.intro-col h2{font-family:"Source Sans 3",sans-serif;font-weight:600;font-size:28px;color:var(--ink);line-height:34px}
.intro-col h2 em{font-style:normal;color:var(--blue)}
.section-rule{height:5px;border-bottom:1px solid var(--rule);position:relative;margin:10px 0 20px}
.section-rule::before{content:"";position:absolute;left:0;top:0;height:4px;background:#ccc}
.col-left{left:92px;width:554px}
.col-left .section-rule{width:532px}
.col-left .section-rule::before{width:338px}
.col-right{left:692px;width:314px}
.col-right .section-rule::before{width:135px}
.intro-col p{font-size:11.2px;line-height:18.5px;color:var(--text);text-align:justify}
.more{display:block;text-align:right;font-family:"Source Sans 3",sans-serif;font-weight:600;font-size:12.5px;color:var(--blue);letter-spacing:.3px;margin-top:18px}
.more b{color:#333;margin-left:4px}
.divider{position:absolute;left:661px;top:31px;height:210px;border-left:1px dotted #999}
.cards{position:absolute;left:0;top:841px;width:1108px}
.card{position:absolute;top:0;width:260px}
.card .photo{height:109px}
.card p{font-size:11.2px;line-height:16.7px;margin-top:13px;text-align:justify}
.card .more{margin-top:18px}
.footer{position:absolute;left:0;top:1085px;width:1108px;height:88px;background:var(--footer)}
.social{position:absolute;top:21px;width:38px;height:38px;border-radius:50%}
.footer-brand{position:absolute;left:494px;top:22px;width:170px;display:flex;align-items:center;gap:8px;font-family:"Source Sans 3",sans-serif;font-weight:600;font-size:16px;line-height:19px;color:var(--footer-mark)}
.footer-brand i{flex:none;width:30px;height:30px;border-radius:50%;background:var(--footer-mark);display:block}
.badge{position:absolute}
.copyright{position:absolute;left:0;top:1173px;width:1108px;height:27px;background:var(--footer-dark);color:#ccc;font-size:12px;text-align:center;line-height:27px}
</style>
</head>
<body>
<header class="site-header">
  <div class="brand"><span class="brand-dot"></span>Meridian Gauging Services</div>
  <nav class="main-nav">HOME<span>|</span>CONTACT</nav>
  <div class="search">search keyword
    <svg width="18" height="18" viewBox="0 0 18 18"><circle cx="7.5" cy="7.5" r="5.5" fill="none" stroke="#2a94c6" stroke-width="2"/><line x1="11.5" y1="11.5" x2="16" y2="16" stroke="#2a94c6" stroke-width="2.4" stroke-linecap="round"/></svg>
  </div>
</header>
<div class="header-rule"></div>

<section class="hero" role="img" aria-label="White fuel storage tanks at a waterfront terminal reflected in calm water">
  <div class="hero-box">
    <h1>Our Expert <em>Technical</em></h1>
    <ul>
      <li>Planned Maintenance</li>
      <li>System calibrations, validations and verification</li>
      <li>System monitoring and repair</li>
      <li>Emergency Breakdowns</li>
      <li>Remote support</li>
      <li>Customer training</li>
    </ul>
  </div>
</section>

<section class="intro">
  <div class="intro-col col-left">
    <h2><em>Meridian Gauging</em> Services</h2>
    <div class="section-rule"></div>
    <p>Lorem ipsum dolor sit amet, consectetur adipiscing elit. Quisque dapibus accumsan orci, pretium eleifend arcu adipiscing eget. Fusce accumsan facilisis tincidunt. Phasellus tempor enim purus, vitae venenatis est. Ut imperdiet hendrerit pulvinar. Cras at tellus a enim condimentum mollis ut et tellus. Mauris dolor magna, elementum eu dictum eu, fermentum a nibh. Praesent ut dui lectus, vel lacinia sem. Praesent commodo malesuada urna, quis convallis risus dictum et. Nunc dapibus interdum libero, et semper eros auctor ac.</p>
    <a class="more" style="margin-top:30px">More Details <b>»</b></a>
  </div>
  <div class="divider"></div>
  <div class="intro-col col-right">
    <h2><em>Service &amp;</em> Maintenance</h2>
    <div class="section-rule" style="margin-top:6px;margin-bottom:12px"></div>
    <p>Our expert technical personnel will ensure that however well the system was installed or how well it worked when it was commissioned, it will remain safe, accurate and reliable through inspections, audits, calibration and validation of your systems to NMTA traceable standards. We have the skills to work on all types of control and process equipment - radar level gauging, servo gauging,</p>
    <a class="more">More Details <b>»</b></a>
  </div>
</section>

<section class="cards">
  <article class="card" style="left:100px">
    <div class="photo" role="img" aria-label="Horizontal storage tanks at dusk" style="background:linear-gradient(180deg,#1c2d55 0%,#d6a060 40%,#dcdcdc 65%,#3a3a3a 100%)"></div>
    <p>Vestibulum rutrum pharetra diam, eget dapibus leo vehicula ut. Fusce aliquam, odio eget adipiscing lobortis, nisl sapien placerat est...</p>
    <a class="more">More Details <b>»</b></a>
  </article>
  <article class="card" style="left:419px">
    <div class="photo" role="img" aria-label="Level gauging transmitter mounted on a tank roof" style="background:linear-gradient(135deg,#c9ccd0 0%,#e0a020 30%,#4d6a85 55%,#eaeaea 100%)"></div>
    <p>Vestibulum rutrum pharetra diam, eget dapibus leo vehicula ut. Fusce aliquam, odio eget adipiscing lobortis, nisl sapien placerat est...</p>
    <a class="more">More Details <b>»</b></a>
  </article>
  <article class="card" style="left:739px">
    <div class="photo" role="img" aria-label="Two technicians in hi-vis gear on an industrial site" style="background:linear-gradient(180deg,#aab8c8 0%,#8a9070 45%,#c8c830 65%,#5a5a50 100%)"></div>
    <p>Vestibulum rutrum pharetra diam, eget dapibus leo vehicula ut. Fusce aliquam, odio eget adipiscing lobortis, nisl sapien placerat est...</p>
    <a class="more" style="margin-right:10px">More Details <b>»</b></a>
  </article>
</section>

<footer class="footer">
  <span class="social" style="left:105px;background:#1d4f7d" aria-label="chirpnest"></span>
  <span class="social" style="left:153px;background:#2aa3e0" aria-label="Social link"></span>
  <span class="social" style="left:201px;background:#f29422" aria-label="RSS feed"></span>
  <span class="social" style="left:249px;background:#bdbdbd" aria-label="Email"></span>
  <div class="footer-brand"><i></i><span>Meridian Gauging Services</span></div>
  <div class="badge" style="left:695px;top:23px;width:192px;height:48px;background:#e6e6e6" aria-label="Partner badge"></div>
  <div class="badge" style="left:948px;top:22px;width:68px;height:50px;background:#777" aria-label="Partner badge"></div>
</footer>
<div class="copyright">Copyright © 2014 Meridian Gauging Services Solutions | Disclaimer</div>
</body>
</html>
```